Long term design collaboration - mobile app design & web app design

We are looking for a talented mobile designer to help us improve our UI & UX for mobile app and web app.

The screens that need to be redesigned are attached.

There is potentially a lot more work in future design available for the successful candidate.
The successful candidate would have to take part in daily stand-up around 3 times per week.
The successful candidate would join a dev team
We are software company that does property management

```html
<!DOCTYPE html>
<html lang="en">
<head>
<meta charset="utf-8">
<title>Property management dashboard</title>
<link href="https://fonts.googleapis.com/css2?family=Poppins:wght@400;500;600;700&display=swap" rel="stylesheet">
<style>
:root{
  --stage:#cdcdcd;--white:#fff;--panel:#eff3f8;--line:#dde3ec;--ink:#1b1d24;--muted:#6b7280;
  --blue:#2a5bc4;--blue-soft:#d3e3fa;--warn-bg:#fff2c4;--warn-line:#f2c94c;--warn:#f0a500;--danger:#e5484d;--ok:#22a35a;--ok-bg:#e3f6ea;
}
*{box-sizing:border-box;margin:0;padding:0}
html,body{width:1200px;height:2409px;overflow:hidden;background:var(--stage)}
body{font-family:'Poppins',sans-serif;color:var(--ink)}
.canvas{position:absolute;left:0;top:0;width:1283px;height:2576px;transform:scale(.93531);transform-origin:0 0}
.abs{position:absolute}
.desk{position:absolute;left:52px;width:1178px;height:838px;background:var(--white)}
.brand{position:absolute;left:62px;top:18px;font-size:25px;font-weight:700;color:var(--blue);letter-spacing:.5px}
.search{position:absolute;left:230px;top:17px;width:408px;height:32px;border:1px solid var(--line);border-radius:6px;font-size:12px;color:var(--muted);padding:7px 9px}
.search svg{position:absolute;right:9px;top:6px}
.bell{position:absolute;left:968px;top:22px}
.avatar{position:absolute;width:32px;height:32px;border-radius:50%;background:linear-gradient(135deg,#6a4a3a,#c49a7a)}
.user{position:absolute;top:17px;font-size:12px;font-weight:500}
.user small{display:block;font-size:10px;color:var(--muted);font-weight:400;margin-top:2px}
.nav{position:absolute;left:10px;top:84px;width:190px}
.nav a{display:flex;align-items:center;gap:10px;height:32px;padding:0 6px;margin-bottom:7.3px;font-size:12px;font-weight:500;color:var(--ink);text-decoration:none;border-radius:5px}
.nav a.active{background:var(--blue);color:#fff}
.nav svg{width:20px;height:20px;fill:none;stroke:currentColor;stroke-width:1.6}
.main{position:absolute;left:210px;top:66px;width:955px;height:759px;background:var(--panel);border-radius:16px;padding:0 20px}
.main h1{font-size:27px;font-weight:700;margin-top:20px;height:40px}
.alert{margin-top:20px;background:var(--warn-bg);border:1px solid var(--warn-line);border-radius:8px;padding:14px 16px 10px;font-size:12px}
.alert .head{color:var(--warn);display:flex;align-items:center;gap:8px;margin-bottom:8px}
.alert .row{display:flex;justify-content:space-between;align-items:center;height:26px}
.tabs{margin-top:26px;display:flex;gap:8px;border-bottom:1px solid var(--line);padding-bottom:12px}
.tab{display:flex;align-items:center;gap:8px;height:32px;padding:0 12px;font-size:14px;color:var(--muted);border-radius:6px}
.tab.on{background:#fff;color:var(--ink);font-weight:500;border:1px solid var(--line)}
.label{font-size:14px;font-weight:500;margin:26px 0 12px}
.table{background:#fff;border:1px solid var(--line);border-radius:8px}
.table .row{display:flex;align-items:center;height:46.5px;padding:0 16px;font-size:12px;border-bottom:1px solid var(--line)}
.table .row:last-child{border-bottom:none}
.table .k{width:154px}
.table .v{flex:1;color:var(--muted)}
.cards{display:flex;gap:14px}
.card{position:relative;background:#fff;border:1px solid var(--line);border-left:3px solid var(--blue);border-radius:8px;height:94px;flex:1;padding:14px 14px;font-size:12px}
.card .t{font-weight:500}
.card .s{color:var(--muted);margin-top:14px;line-height:1.35}
.card .ic{position:absolute;right:14px;top:15px}
.box{background:#fff;border:1px solid var(--line);border-radius:8px;padding:16px;position:relative;font-size:14px;font-weight:500}
.more{position:absolute;right:18px;bottom:14px;font-size:10px;color:var(--muted);font-weight:400;display:flex;align-items:center;gap:6px}
.pill{position:absolute;right:16px;top:16px;background:var(--ok-bg);color:var(--ok);font-size:10px;font-weight:400;border-radius:10px;padding:2px 8px 2px 18px}
.pill:before{content:"";position:absolute;left:7px;top:7px;width:6px;height:6px;border-radius:50%;background:var(--ok)}
.phone{position:absolute;top:1833px;width:320px;height:691px;background:var(--panel);overflow:hidden}
.bar{position:absolute;left:0;top:0;width:100%;height:83px;background:#fff}
.time{position:absolute;left:38px;top:12px;font-size:14px;font-weight:600}
.sig{position:absolute;right:22px;top:15px}
.ptitle{position:absolute;left:16px;top:50px;font-size:15px;font-weight:600;display:flex;align-items:center;gap:12px}
.pbody{position:absolute;left:13px;top:101px;width:293px}
.pbody .label{margin:0 0 12px;font-size:13px}
.mrow{height:61px;display:flex;align-items:center;justify-content:space-between;padding:0 12px;border-bottom:1px solid var(--line);font-size:12px}
.mrow .v{color:var(--muted);display:block;margin-top:2px}
.mcards{display:grid;grid-template-columns:1fr 1fr;gap:14px}
.mcards .card{height:77px;padding:12px 14px}
.mcards .card .s{margin-top:10px}
.tabbar{position:absolute;left:0;bottom:0;width:100%;height:66px;background:#fff;display:flex;justify-content:space-around;padding-top:12px}
.tabbar div{display:flex;flex-direction:column;align-items:center;gap:3px;font-size:9px;color:var(--muted)}
.tabbar .on{color:var(--blue)}
.fin{background:#fff;border:1px solid var(--line);border-radius:6px;height:48px;display:flex;align-items:center;padding:0 10px 0 8px;gap:10px;font-size:11px;margin-bottom:8px}
.fin .i{width:32px;height:32px;border-radius:4px;background:var(--blue-soft);display:flex;align-items:center;justify-content:center}
.fin .n{flex:1;font-weight:500}
.fin .n small{display:block;font-size:9px;color:var(--muted);font-weight:400}
.fin .amt{font-size:14px;font-weight:600}
.opt{height:44px;background:#fff;border:1px solid var(--line);border-radius:6px;display:flex;align-items:center;gap:10px;padding:0 8px;font-size:11px;margin-bottom:8px}
.opt i{width:13px;height:13px;border-radius:50%;border:1px solid #9aa3b0;display:block}
.opt.sel{background:var(--blue-soft);border-color:var(--blue)}
.opt.sel i{border-color:var(--blue);background:radial-gradient(circle,var(--blue) 55%,#fff 60%)}
.foot{position:absolute;left:0;bottom:0;width:100%;height:66px;background:#fff}
.btn{position:absolute;top:11px;height:32px;border-radius:5px;font-size:11px;display:flex;align-items:center;justify-content:center;gap:6px;font-weight:500}
.btn.back{left:160px;width:71px;border:1px solid var(--line)}
.btn.next{left:238px;width:68px;background:var(--blue);color:#fff}
</style>
</head>
<body>
<div class="canvas">

<!-- Desktop overview -->
<section class="desk" style="top:52px">
  <div class="brand">ORVANE</div>
  <div class="search">Search<svg width="18" height="18" viewBox="0 0 20 20" fill="none" stroke="#444" stroke-width="1.6"><circle cx="9" cy="9" r="7"/><path d="M14 14l4 4"/></svg></div>
  <svg class="bell" width="20" height="20" viewBox="0 0 20 20" fill="none" stroke="#222" stroke-width="1.5"><path d="M5 14V9a5 5 0 0110 0v5l1.5 1.5h-13z"/><path d="M8 17.5a2 2 0 004 0"/></svg>
  <div class="avatar" role="img" aria-label="User profile photo" style="left:1008px;top:17px"></div>
  <div class="user" style="left:1050px">Clara Benton<small>My Account</small></div>
  <nav class="nav">
    <a href="#"><svg viewBox="0 0 20 20"><circle cx="8" cy="7" r="3.5"/><path d="M2 17c1-3.5 3.5-5 6-5s5 1.5 6 5"/><path d="M13 4a3 3 0 010 6"/></svg>User Directory</a>
    <a href="#"><svg viewBox="0 0 20 20"><path d="M3 7h14l-4-4M17 13H3l4 4"/></svg>Switch Development</a>
    <a href="#"><svg viewBox="0 0 20 20"><path d="M4 3h12v15l-6-4-6 4z"/></svg>Service Change</a>
    <a href="#"><svg viewBox="0 0 20 20"><path d="M5 2h7l4 4v12H5z"/><path d="M8 9h5M8 12h5M8 15h3"/></svg>Property Balance</a>
    <a href="#" class="active"><svg viewBox="0 0 20 20"><rect x="2" y="4" width="16" height="12" rx="1"/><path d="M2 5l8 6 8-6M2 15l6-5M18 15l-6-5"/></svg>Sending Letter</a>
    <a href="#"><svg viewBox="0 0 20 20"><path d="M5 2h7l4 4v12H5z"/><path d="M12 2v4h4"/></svg>Regular Service</a>
  </nav>
  <main class="main">
    <h1>Overview</h1>
    <div class="alert">
      <div class="head"><svg width="18" height="18" viewBox="0 0 20 20" fill="none" stroke="#f0a500" stroke-width="1.5"><circle cx="10" cy="10" r="8"/><path d="M10 6v5M10 13.5v.5"/></svg>Please complete basic setup</div>
      <div class="row">Service charge schedules<svg width="12" height="12" viewBox="0 0 12 12" fill="none" stroke="#222" stroke-width="1.5"><path d="M4 2l4 4-4 4"/></svg></div>
      <div class="row">Service charge appointment<svg width="12" height="12" viewBox="0 0 12 12" fill="none" stroke="#222" stroke-width="1.5"><path d="M4 2l4 4-4 4"/></svg></div>
      <div class="row">Invite resident &amp; leaseholder<svg width="12" height="12" viewBox="0 0 12 12" fill="none" stroke="#222" stroke-width="1.5"><path d="M4 2l4 4-4 4"/></svg></div>
      <div class="row">Connect payment provider<svg width="12" height="12" viewBox="0 0 12 12" fill="none" stroke="#222" stroke-width="1.5"><path d="M4 2l4 4-4 4"/></svg></div>
    </div>
    <div class="tabs">
      <div class="tab on"><svg width="18" height="18" viewBox="0 0 20 20" fill="none" stroke="#333" stroke-width="1.4"><path d="M4 2h12v16H4z"/><path d="M7 6h6M7 9h6M7 13l2 2 3-3"/></svg>Summary</div>
      <div class="tab"><svg width="18" height="18" viewBox="0 0 20 20" fill="none" stroke="#555" stroke-width="1.4"><path d="M13 18H4V2h12v9"/><path d="M7 6h6M7 9h4"/><circle cx="14" cy="15" r="2.5"/><path d="M16 17l2 2"/></svg>Details</div>
    </div>
    <div class="label">General</div>
    <div class="table">
      <div class="row"><span class="k">Units</span><span class="v">85</span><svg width="12" height="12" viewBox="0 0 12 12" fill="none" stroke="#333" stroke-width="1.4"><path d="M4 2l4 4-4 4"/></svg></div>
      <div class="row"><span class="k">Handover Date</span><span class="v">12 January 2023</span><svg width="12" height="12" viewBox="0 0 12 12" fill="none" stroke="#333" stroke-width="1.4"><path d="M4 2l4 4-4 4"/></svg></div>
      <div class="row"><span class="k">Address</span><span class="v">24 Elm Grove Road, Leeds, LS6 2QT</span><svg width="12" height="12" viewBox="0 0 12 12" fill="none" stroke="#333" stroke-width="1.4"><path d="M4 2l4 4-4 4"/></svg></div>
      <div class="row"><span class="k">Section Limit</span><span class="v">$20</span></div>
    </div>
    <div class="label" style="margin-top:30px">Compliance</div>
    <div class="cards">
      <div class="card"><div class="t">Asbestos</div><div class="s">NA</div></div>
      <div class="card"><div class="t">Legionellas</div><svg class="ic" width="16" height="16" viewBox="0 0 20 20" fill="none" stroke="#f0a500" stroke-width="1.5"><circle cx="10" cy="10" r="8"/><path d="M8 8a2 2 0 114 0c0 1.5-2 1.5-2 3M10 14v.5"/></svg><div class="s">-</div></div>
      <div class="card"><div class="t">Drains</div><svg class="ic" width="16" height="16" viewBox="0 0 20 20" fill="none" stroke="#e5484d" stroke-width="1.5"><circle cx="10" cy="10" r="8"/><path d="M10 6v5M10 13.5v.5"/></svg><div class="s">Overdue<br>10 December 2023</div></div>
      <div class="card"><div class="t">Gutters</div><div class="s">NA</div></div>
      <div class="card"><div class="t">Dry Risers</div><div class="s">NA</div></div>
    </div>
  </main>
</section>

<!-- Desktop finances -->
<section class="desk" style="top:943px">
  <div class="brand">ORVANE</div>
  <div class="search">Search<svg width="18" height="18" viewBox="0 0 20 20" fill="none" stroke="#444" stroke-width="1.6"><circle cx="9" cy="9" r="7"/><path d="M14 14l4 4"/></svg></div>
  <svg class="bell" style="left:963px" width="20" height="20" viewBox="0 0 20 20" fill="none" stroke="#222" stroke-width="1.5"><path d="M5 14V9a5 5 0 0110 0v5l1.5 1.5h-13z"/><path d="M8 17.5a2 2 0 004 0"/></svg>
  <div class="avatar" role="img" aria-label="User profile photo" style="left:1003px;top:17px"></div>
  <div class="user" style="left:1045px">Clara Benton<small>Development Manager</small></div>
  <nav class="nav">
    <a href="#"><svg viewBox="0 0 20 20"><circle cx="8" cy="7" r="3.5"/><path d="M2 17c1-3.5 3.5-5 6-5s5 1.5 6 5"/><path d="M13 4a3 3 0 010 6"/></svg>User Directory</a>
    <a href="#"><svg viewBox="0 0 20 20"><path d="M3 7h14l-4-4M17 13H3l4 4"/></svg>Switch Development</a>
    <a href="#"><svg viewBox="0 0 20 20"><path d="M4 3h12v15l-6-4-6 4z"/></svg>Service Change</a>
    <a href="#"><svg viewBox="0 0 20 20"><path d="M5 2h7l4 4v12H5z"/><path d="M8 9h5M8 12h5M8 15h3"/></svg>Property Balance</a>
    <a href="#" class="active"><svg viewBox="0 0 20 20"><rect x="2" y="4" width="16" height="12" rx="1"/><path d="M2 5l8 6 8-6M2 15l6-5M18 15l-6-5"/></svg>Sending Letter</a>
    <a href="#"><svg viewBox="0 0 20 20"><path d="M5 2h7l4 4v12H5z"/><path d="M12 2v4h4"/></svg>Regular Service</a>
  </nav>
  <main class="main">
    <h1>Finances</h1>
    <div class="box" style="margin-top:20px;height:78px">Subaccount<span class="more">View Details<svg width="8" height="8" viewBox="0 0 12 12" fill="none" stroke="#333" stroke-width="1.6"><path d="M4 2l4 4-4 4"/></svg></span></div>
    <div class="box" style="margin-top:14px;height:81px">Payment Provider<span class="pill">Connected</span><span class="more">View Details<svg width="8" height="8" viewBox="0 0 12 12" fill="none" stroke="#333" stroke-width="1.6"><path d="M4 2l4 4-4 4"/></svg></span></div>
  </main>
</section>

<!-- Mobile overview -->
<section class="phone" style="left:52px">
  <div class="bar">
    <div class="time">9:41</div>
    <svg class="sig" width="64" height="12" viewBox="0 0 64 12"><rect x="0" y="8" width="3" height="4" fill="#111"/><rect x="5" y="6" width="3" height="6" fill="#111"/><rect x="10" y="3" width="3" height="9" fill="#111"/><rect x="15" y="0" width="3" height="12" fill="#111"/><path d="M24 5a10 10 0 0114 0M27 8a5 5 0 018 0" stroke="#111" stroke-width="1.8" fill="none"/><circle cx="31" cy="10.5" r="1.3" fill="#111"/><rect x="42" y="1" width="19" height="10" rx="3" fill="none" stroke="#999"/><rect x="44" y="3" width="15" height="6" rx="1" fill="#111"/></svg>
    <div class="ptitle"><svg width="12" height="12" viewBox="0 0 12 12" fill="none" stroke="#111" stroke-width="1.6"><path d="M8 2L4 6l4 4"/></svg>Development Overview</div>
  </div>
  <div class="pbody">
    <div class="label">General</div>
    <div class="table">
      <div class="mrow"><div>Units<span class="v">85</span></div><svg width="12" height="12" viewBox="0 0 12 12" fill="none" stroke="#333" stroke-width="1.4"><path d="M4 2l4 4-4 4"/></svg></div>
      <div class="mrow"><div>Handover Date<span class="v">12 January 2023</span></div><svg width="12" height="12" viewBox="0 0 12 12" fill="none" stroke="#333" stroke-width="1.4"><path d="M4 2l4 4-4 4"/></svg></div>
      <div class="mrow"><div>Address<span class="v">24 Elm Grove Road, Leeds, LS6 2QT</span></div><svg width="12" height="12" viewBox="0 0 12 12" fill="none" stroke="#333" stroke-width="1.4"><path d="M4 2l4 4-4 4"/></svg></div>
      <div class="mrow" style="height:42px;border-bottom:none">Section Limit<span class="v">$20</span></div>
    </div>
    <div class="label" style="margin-top:22px">Compliance</div>
    <div class="mcards">
      <div class="card"><div class="t">Asbestos</div><div class="s">NA</div></div>
      <div class="card"><div class="t">Legionellas</div><svg class="ic" width="16" height="16" viewBox="0 0 20 20" fill="none" stroke="#f0a500" stroke-width="1.5"><circle cx="10" cy="10" r="8"/><path d="M8 8a2 2 0 114 0c0 1.5-2 1.5-2 3M10 14v.5"/></svg><div class="s">-</div></div>
      <div class="card" style="height:94px"><div class="t">Drains</div><svg class="ic" width="16" height="16" viewBox="0 0 20 20" fill="none" stroke="#e5484d" stroke-width="1.5"><circle cx="10" cy="10" r="8"/><path d="M10 6v5M10 13.5v.5"/></svg><div class="s">Overdue<br>10 December 2023</div></div>
      <div class="card" style="height:94px"><div class="t">Gutters</div><div class="s">NA</div></div>
      <div class="card" style="grid-column:1/3;height:40px"></div>
    </div>
  </div>
  <nav class="tabbar">
    <div class="on"><svg width="20" height="20" viewBox="0 0 20 20" fill="none" stroke="currentColor" stroke-width="1.5"><path d="M3 9l7-6 7 6v8H3z"/><path d="M8 17v-5h4v5"/></svg>Home</div>
    <div><svg width="20" height="20" viewBox="0 0 20 20" fill="none" stroke="currentColor" stroke-width="1.5"><rect x="3" y="3" width="14" height="14" rx="2"/><path d="M7 13V9M10 13V6M13 13v-2"/></svg>Overview</div>
    <div><svg width="20" height="20" viewBox="0 0 20 20" fill="none" stroke="currentColor" stroke-width="1.5"><rect x="2" y="4" width="16" height="12" rx="2"/><path d="M2 8h16M5 12h4"/></svg>Finances</div>
    <div><svg width="20" height="20" viewBox="0 0 20 20" fill="none" stroke="currentColor" stroke-width="1.5"><path d="M3 3h14v10H8l-4 4V3z"/><path d="M6 7h8M6 10h5"/></svg>Messages</div>
  </nav>
</section>

<!-- Mobile finances -->
<section class="phone" style="left:482px">
  <div class="bar">
    <div class="time">9:41</div>
    <svg class="sig" width="64" height="12" viewBox="0 0 64 12"><rect x="0" y="8" width="3" height="4" fill="#111"/><rect x="5" y="6" width="3" height="6" fill="#111"/><rect x="10" y="3" width="3" height="9" fill="#111"/><rect x="15" y="0" width="3" height="12" fill="#111"/><path d="M24 5a10 10 0 0114 0M27 8a5 5 0 018 0" stroke="#111" stroke-width="1.8" fill="none"/><circle cx="31" cy="10.5" r="1.3" fill="#111"/><rect x="42" y="1" width="19" height="10" rx="3" fill="none" stroke="#999"/><rect x="44" y="3" width="15" height="6" rx="1" fill="#111"/></svg>
    <div class="ptitle"><svg width="12" height="12" viewBox="0 0 12 12" fill="none" stroke="#111" stroke-width="1.6"><path d="M8 2L4 6l4 4"/></svg>Finances</div>
  </div>
  <div class="pbody">
    <div class="label">Account Receivable</div>
    <div class="fin"><span class="i"><svg width="18" height="18" viewBox="0 0 20 20" fill="none" stroke="#2a5bc4" stroke-width="1.4"><circle cx="11" cy="6" r="3"/><path d="M2 12h4l3 2h5l3-2v4H2z"/></svg></span><span class="n">Arrears<small>5 bills</small></span><span class="amt">$7,268</span><svg width="12" height="12" viewBox="0 0 12 12" fill="none" stroke="#333" stroke-width="1.4"><path d="M4 2l4 4-4 4"/></svg></div>
    <div class="fin"><span class="i"><svg width="18" height="18" viewBox="0 0 20 20" fill="none" stroke="#2a5bc4" stroke-width="1.4"><path d="M4 3h12v15l-6-4-6 4z"/></svg></span><span class="n">Unallocated Receipts<small>5 receipt</small></span><span class="amt">$7,268</span><svg width="12" height="12" viewBox="0 0 12 12" fill="none" stroke="#333" stroke-width="1.4"><path d="M4 2l4 4-4 4"/></svg></div>
    <div class="label" style="margin-top:28px">Accounts Payable</div>
    <div class="fin"><span class="i"><svg width="18" height="18" viewBox="0 0 20 20" fill="none" stroke="#2a5bc4" stroke-width="1.4"><rect x="2" y="5" width="16" height="10" rx="1"/><circle cx="10" cy="10" r="2"/></svg></span><span class="n">Invoices<small>5 invoices</small></span><span class="amt">$7,268</span><svg width="12" height="12" viewBox="0 0 12 12" fill="none" stroke="#333" stroke-width="1.4"><path d="M4 2l4 4-4 4"/></svg></div>
  </div>
</section>

<!-- Mobile question -->
<section class="phone" style="left:911px">
  <div class="bar">
    <div class="time">9:41</div>
    <svg class="sig" width="64" height="12" viewBox="0 0 64 12"><rect x="0" y="8" width="3" height="4" fill="#111"/><rect x="5" y="6" width="3" height="6" fill="#111"/><rect x="10" y="3" width="3" height="9" fill="#111"/><rect x="15" y="0" width="3" height="12" fill="#111"/><path d="M24 5a10 10 0 0114 0M27 8a5 5 0 018 0" stroke="#111" stroke-width="1.8" fill="none"/><circle cx="31" cy="10.5" r="1.3" fill="#111"/><rect x="42" y="1" width="19" height="10" rx="3" fill="none" stroke="#999"/><rect x="44" y="3" width="15" height="6" rx="1" fill="#111"/></svg>
    <div class="ptitle"><svg width="12" height="12" viewBox="0 0 12 12" fill="none" stroke="#111" stroke-width="1.6"><path d="M8 2L4 6l4 4"/></svg>Legionellas</div>
  </div>
  <div class="pbody">
    <div class="label">Is it reuired?</div>
    <div class="opt"><i></i>No</div>
    <div class="opt"><i></i>Yes, but I do not have a file to upload</div>
    <div class="opt sel"><i></i>Yes, and I have a file to upload</div>
  </div>
  <div class="foot">
    <div class="btn back"><svg width="10" height="10" viewBox="0 0 12 12" fill="none" stroke="#111" stroke-width="1.8"><path d="M8 2L4 6l4 4"/></svg>Back</div>
    <div class="btn next">Next<svg width="10" height="10" viewBox="0 0 12 12" fill="none" stroke="#fff" stroke-width="1.8"><path d="M4 2l4 4-4 4"/></svg></div>
  </div>
</section>

</div>
</body>
</html>
```